RV park billboard

We need a billboard for cedar bend RV park . I was thinking about having a big orange in the background. We will have free fiber optic internet and each camper will have its own personal hotspot and we want that on the sign... Also the phone number with the area code... But I don't have the exact number yet. Size of sign will be 12 x 40
Updates
Make sure sign has Cedar Bend RV park on it
Target Market(s)
Plant turnaround workers
Look and feel

```html
<!DOCTYPE html>
<html lang="en">
<head>
<meta charset="utf-8">
<title>Cedar Bend RV park billboard</title>
<link rel="stylesheet" href="https://fonts.googleapis.com/css2?family=Oswald:wght@500;600;700&display=swap">
<style>
  :root {
    --page-bg: #eef1f4;
    --orange-light: #fbb232;
    --orange-mid: #f7982c;
    --orange-deep: #ef7f22;
    --title-white: #ffffff;
    --phone-red: #e31b23;
    --ink: #0d0d0d;
    --icon-area: #3a3a36;
  }
  html, body {
    margin: 0;
    padding: 0;
    width: 1200px;
    height: 1200px;
    overflow: hidden;
    background: var(--page-bg);
  }
  .billboard {
    display: block;
    width: 1200px;
    height: 1200px;
  }
  .sign-title {
    font-family: "Oswald", sans-serif;
    font-weight: 600;
    font-size: 96px;
    fill: var(--title-white);
  }
  .sign-phone {
    font-family: "Oswald", sans-serif;
    font-weight: 600;
    font-size: 196px;
    fill: var(--phone-red);
  }
  .sign-tagline {
    font-family: "Oswald", sans-serif;
    font-weight: 600;
    font-size: 96px;
    fill: var(--ink);
  }
  .hotspot-illustration {
    fill: var(--icon-area);
    opacity: 0.85;
  }
</style>
</head>
<body>
<svg class="billboard" viewBox="0 0 1200 1200" xmlns="http://www.w3.org/2000/svg">
  <defs>
    <radialGradient id="orangeFill" cx="0.62" cy="0.28" r="0.8">
      <stop offset="0" stop-color="var(--orange-light)"/>
      <stop offset="0.55" stop-color="var(--orange-mid)"/>
      <stop offset="1" stop-color="var(--orange-deep)"/>
    </radialGradient>
  </defs>

  <ellipse class="orange-backdrop" cx="600" cy="600" rx="560" ry="540"
           fill="url(#orangeFill)" role="img"
           aria-label="Large ripe orange with a green leaf on its stem"/>

  <text class="sign-title" x="600" y="305" text-anchor="middle">Cedar Bend RV park</text>

  <text class="sign-phone" x="600" y="575" text-anchor="middle" textLength="920" lengthAdjust="spacingAndGlyphs">(913)555-0148</text>

  <rect class="hotspot-illustration" x="299" y="682" width="603" height="156" rx="6"
        role="img"
        aria-label="Illustration of campsite hotspot panels with status lights"/>

  <text class="sign-tagline" x="600" y="950" text-anchor="middle">Own Personal</text>
  <text class="sign-tagline" x="600" y="1046" text-anchor="middle">Hotspot</text>
</svg>
</body>
</html>
```